Product Line - Label & Logo design

Logo & label design for a supplement line we are developing . The product name is BROVEN ( qtz ) We would like a white jar with a purple metalic lid and somehow blend in the lettering/wording . I will attach sample products to view. Feel free to add in the boxes of the label with the numbers from the sample label. We can correct once we have the design completed. Feel free to change the lettering style, shape etc

Target Market(s)

Supplement / exercise

Industry/Entity Type

Fitness

Colors
6B429C
8869AF
B7A5CE
E3DAEB
F3F0F8

```html
<!DOCTYPE html>
<html lang="en">
<head>
<meta charset="utf-8">
<title>BROVEN Preworkout Label</title>
<link rel="stylesheet" href="https://fonts.googleapis.com/css2?family=Jost:wght@400;500;700&display=swap">
<style>
  :root {
    --purple-deep: #6B429C;
    --purple-mid: #8869AF;
    --lilac: #B7A5CE;
    --mist: #E3DAEB;
    --pale: #F3F0F8;
    --white: #ffffff;
    --accent-pink: #e6a8f5;
  }
  * { margin: 0; padding: 0; box-sizing: border-box; }
  html, body { width: 1200px; height: 1041px; overflow: hidden; }
  body {
    position: relative;
    font-family: "Jost", sans-serif;
    background: linear-gradient(180deg, #c9b3e8 0%, var(--mist) 70%, #e6dfee 100%);
  }
  .backdrop-wordmark {
    position: absolute;
    left: 50%;
    top: 520px;
    transform: translate(-50%, -50%);
    font-weight: 700;
    font-size: 290px;
    line-height: 1;
    letter-spacing: 40px;
    color: var(--purple-deep);
    white-space: nowrap;
  }
  .label {
    position: absolute;
    left: 369px;
    top: 296px;
    width: 466px;
    height: 546px;
    border-radius: 46px;
    background: linear-gradient(135deg, #f7f7f7 0%, var(--white) 35%, #e9e9e9 100%);
    overflow: hidden;
  }
  .label-art { position: absolute; inset: 0; }
  .wordmark {
    position: absolute;
    left: 42px;
    top: 158px;
    width: 381px;
    text-align: center;
    font-weight: 700;
    font-size: 86px;
    line-height: 1;
    letter-spacing: 6px;
    color: var(--purple-deep);
  }
  .product-band {
    position: absolute;
    left: 42px;
    top: 244px;
    width: 381px;
    height: 26px;
    background: var(--purple-deep);
    color: var(--white);
    font-weight: 500;
    font-size: 19px;
    line-height: 26px;
    letter-spacing: 3.4px;
    text-align: center;
  }
  .dose-grid {
    position: absolute;
    left: 331px;
    top: 343px;
    display: grid;
    grid-template-columns: 41px 40px;
    column-gap: 11px;
    row-gap: 11px;
  }
  .dose {
    height: 38px;
    background: var(--purple-deep);
    color: var(--white);
    text-align: center;
    padding-top: 2px;
  }
  .dose-amount { font-size: 21px; font-weight: 500; line-height: 1; }
  .dose-amount small { font-size: 10px; }
  .dose-name { font-size: 5.5px; font-weight: 500; letter-spacing: 0.2px; margin-top: 3px; }
  .net-weight {
    position: absolute;
    right: 44px;
    top: 488px;
    font-weight: 700;
    font-size: 17px;
    color: var(--purple-deep);
  }
  .supplement-note {
    position: absolute;
    right: 44px;
    top: 510px;
    font-size: 12px;
    color: var(--purple-deep);
    letter-spacing: 0.3px;
  }
</style>
</head>
<body>
  <div class="backdrop-wordmark">BROVEN</div>

  <section class="label">
    <svg class="label-art" width="466" height="546" viewBox="0 0 466 546">
      <defs>
        <linearGradient id="meshTone" x1="0" y1="0" x2="1" y2="1">
          <stop offset="0" stop-color="#f0d8f7" stop-opacity="0"/>
          <stop offset="0.45" stop-color="#d9b8f0" stop-opacity="0.55"/>
          <stop offset="1" stop-color="#f0d8f7" stop-opacity="0"/>
        </linearGradient>
        <linearGradient id="lineTone" x1="0" y1="0" x2="1" y2="0">
          <stop offset="0" stop-color="#9b5fe0"/>
          <stop offset="0.5" stop-color="var(--accent-pink)"/>
          <stop offset="1" stop-color="#9b5fe0"/>
        </linearGradient>
      </defs>
      <polygon role="img" aria-label="Hexagon mesh pattern band" fill="url(#meshTone)"
               points="0,30 90,30 466,330 466,520 380,520 0,220"/>
      <g fill="none" stroke="url(#lineTone)" stroke-width="2.5">
        <polyline points="264,1 466,137"/>
        <polyline points="311,35 311,92 466,195"/>
        <polyline points="0,247 150,340 150,398"/>
        <polyline points="0,304 215,443 215,546"/>
      </g>
    </svg>

    <div class="wordmark">BROVEN</div>
    <div class="product-band">PREWORKOUT SUPPLEMENTS</div>

    <div class="dose-grid">
      <div class="dose"><div class="dose-amount">8<small>G</small></div><div class="dose-name">CITRULINE</div></div>
      <div class="dose"><div class="dose-amount">2<small>G</small></div><div class="dose-name">NITRA-T</div></div>
      <div class="dose"><div class="dose-amount">276<small>MG</small></div><div class="dose-name">CLEANCAF</div></div>
      <div class="dose"><div class="dose-amount">2<small>G</small></div><div class="dose-name">HYDRAMAX</div></div>
    </div>

    <div class="net-weight">510G</div>
    <div class="supplement-note">DIETARY SUPPLEMENT</div>
  </section>
</body>
</html>
```